Tango Holiday Website Needs a Header Design

I'm looking for a talented designer to create an attractive header for my website: http://brightwaltzhaus.de/. I only want a Header Design. The website and everything else should stay the same.
We will be offering vacations for people who want to come to Tenerife to learn and dance Argentine tango. There will be lessons during the day and dancing during the evening. Tenerife is a warm and sunny destination.
The header should blend in well with the background and the images. The current dimentions fo the header is 960 x 160 pixels.
I like the design on a similar website: http://elvientobaile.de/.
Here are some images on google for tango holiday that might help: http://qk.ly/7xRm41P
I'm flexible with colours and am looking forward to your suggestions.
Tango dancers between the ages of 40 and 65
1 page

```html
<!DOCTYPE html>
<html lang="de">
<head>
<meta charset="utf-8">
<title>Bright Waltz Haus – Tango Urlaub auf Teneriffa</title>
<link rel="stylesheet" href="https://fonts.googleapis.com/css2?family=Roboto:wght@300;400&family=Cinzel:wght@400&family=Arimo:wght@400&display=swap">
<style>
  :root {
    --backdrop: #f3f2f2;
    --page: #ffffff;
    --accent: #ef7a52;
    --accent-deep: #d2513a;
    --nav-band: #8b8181;
    --nav-active: #1f1f1f;
    --nav-link: #574f4f;
    --ink: #111111;
    --text: #454545;
    --muted-circle: #ebe9e9;
  }
  html, body {
    margin: 0;
    padding: 0;
    width: 1200px;
    height: 913px;
    overflow: hidden;
    background: var(--backdrop);
  }
  .stage {
    position: relative;
    width: 1259px;
    height: 958px;
    transform: scale(0.9531);
    transform-origin: 0 0;
  }
  .page {
    position: absolute;
    left: 148px;
    top: 26px;
    width: 960px;
    height: 940px;
    background: var(--page);
    box-shadow: 0 0 4px rgba(0,0,0,0.45);
  }
  .site-header {
    position: relative;
    height: 160px;
  }
  .header-rule {
    position: absolute;
    top: 73px;
    height: 3px;
    background: var(--accent);
  }
  .header-rule.left { left: 0; width: 73px; }
  .header-rule.right { left: 674px; width: 286px; }
  .brand {
    position: absolute;
    left: 80px;
    top: 50px;
    width: 440px;
  }
  .brand-name {
    font-family: "Cinzel", serif;
    font-weight: 400;
    font-size: 35px;
    line-height: 44px;
    letter-spacing: 1px;
    color: var(--ink);
    margin: 0;
    white-space: nowrap;
  }
  .brand-tagline {
    font-family: "Cinzel", serif;
    font-size: 15px;
    letter-spacing: 1.5px;
    color: var(--accent-deep);
    margin: 10px 0 0 2px;
    white-space: nowrap;
  }
  .brand-mark {
    position: absolute;
    left: 527px;
    top: 9px;
    width: 136px;
    height: 136px;
    border-radius: 50%;
    background: var(--muted-circle);
  }
  .main-nav {
    height: 35px;
    background: var(--nav-band);
    display: flex;
    align-items: center;
    padding-left: 40px;
    gap: 25px;
    font-family: "Arimo", sans-serif;
    font-size: 14px;
  }
  .main-nav a { text-decoration: none; color: var(--nav-link); }
  .main-nav a.current { color: var(--nav-active); }
  .slider {
    position: absolute;
    left: 20px;
    top: 261px;
    width: 695px;
    height: 348px;
    background: linear-gradient(100deg, #2f4a55 0%, #3c5560 30%, #8a6a55 48%, #c7a58a 62%, #e9e6e2 80%, #3b5058 100%);
  }
  .slider-dots {
    position: absolute;
    left: 307px;
    top: 622px;
    display: flex;
    gap: 8px;
  }
  .slider-dots span {
    width: 8px;
    height: 8px;
    border: 1.5px solid #111;
    border-radius: 50%;
  }
  .slider-dots span.active { background: #111; }
  .content {
    position: absolute;
    left: 49px;
    top: 676px;
    width: 660px;
    font-family: "Roboto", sans-serif;
    font-weight: 300;
    color: var(--text);
  }
  .content h1 {
    font-weight: 400;
    font-size: 22px;
    color: #2b2b2b;
    margin: 0 0 20px;
    letter-spacing: -0.3px;
  }
  .content p {
    font-size: 15px;
    line-height: 21px;
    margin: 0 0 20px;
  }
  .side-photo { position: absolute; left: 757px; }
  .side-photo.coast {
    top: 235px; width: 175px; height: 300px;
    background: linear-gradient(180deg, #2f6c80 0%, #3d7a8c 55%, #6c6258 80%, #8b7a68 100%);
  }
  .side-photo.ballroom {
    top: 575px; width: 178px; height: 163px;
    background: linear-gradient(90deg, #b56a45 0%, #d9cfc6 45%, #f0ece8 65%, #2e3444 100%);
  }
  .highlights {
    position: absolute;
    left: 757px;
    top: 796px;
    margin: 0;
    padding: 0;
    list-style: none;
    font-family: "Arimo", sans-serif;
    font-size: 12.5px;
    line-height: 19px;
    color: var(--text);
  }
  .highlights li::before { content: "*"; display: inline-block; width: 13px; }
</style>
</head>
<body>
<div class="stage">
  <div class="page">
    <header class="site-header">
      <div class="header-rule left"></div>
      <div class="header-rule right"></div>
      <div class="brand">
        <p class="brand-name">Bright Waltz Haus</p>
        <p class="brand-tagline">Tango Holidays in Tenerife</p>
      </div>
      <div class="brand-mark"></div>
    </header>
    <nav class="main-nav">
      <a class="current" href="#">Homepage</a>
      <a href="#">Anbieter von Tango Reisen</a>
      <a href="#">Kontakt</a>
    </nav>

    <div class="slider" role="img" aria-label="Tanzpaar in enger Umarmung vor dem Meer"></div>
    <div class="slider-dots">
      <span></span><span></span><span class="active"></span><span></span><span></span><span></span><span></span>
    </div>

    <section class="content">
      <h1>Tango Urlaub auf Teneriffa</h1>
      <p>„Tanzen ist träumen mit den Beinen“</p>
      <p>Jeder, der bereits einmal einen Tanzkurs besucht hat, weiß, dass in diesem finnischen Sprichwort mehr als nur ein Quäntchen Wahrheit steckt. Für Außenstehende mag es so aussehen, als bewege man sich lediglich zur Musik, ein rhythmisches Miteinander der Tanzpartner, für die Tänzer ist jeder Tanz jedoch einzigartig und etwas ganz Besonderes. Die einzelnen Schritte bilden eine harmonische Abfolge an Bewegungen, jede Geste ist sorgsam durchdacht und wird voller Hingabe ausgeführt. Tanzen bedeutet sich in der Musik zu verlieren, seiner ganzen Leidenschaft Ausdruck zu verleihen und dem Partner blind zu vertrauen.</p>
    </section>

    <div class="side-photo coast" role="img" aria-label="Tanzpaar auf Felsen an der Küste"></div>
    <div class="side-photo ballroom" role="img" aria-label="Lachendes Tanzpaar auf einer Milonga"></div>

    <ul class="highlights">
      <li>Mehr als 40 Stunden Tanz</li>
      <li>Drei Veranstaltungsorte</li>
      <li>Wunderschöne Musik</li>
      <li>Internationale DJs</li>
      <li>Tänzerinnen und Tänzern</li>
      <li>Verhalten</li>
      <li>„Mirada y Cabeceo“</li>
    </ul>
  </div>
</div>
</body>
</html>
```